Party Game Needs Label Design

We need a label design for an innovative party game that combines the fun of peeling off labels with grabbing a cold beverage from a cooler. The label is manufactured to peel off easily (like coupons on products in a grocery store). The inside of the label contains a hidden message, which will direct a party game. The outside of the label should build anticipation/convey fun of peeling off the label to reveal the message. The label is 1.5" wide and 2" tall. The color scheme should be bright and cheerful.
Industry/Entity Type
Grocery Store

```html
<!DOCTYPE html>
<html lang="en">
<head>
<meta charset="utf-8">
<title>Peel Me Party Label</title>
<link rel="stylesheet" href="https://fonts.googleapis.com/css2?family=Rammetto+One&family=Roboto+Mono:wght@500&display=swap">
<style>
  :root {
    --page-bg: #efe6e6;
    --label-shadow: rgba(40, 20, 30, 0.35);
    --scene-dark: #1c0d08;
    --scene-orange: #d9731f;
    --scene-amber: #f3b347;
    --scene-purple: #7b3ca6;
    --scene-pink: #d56bd6;
    --scene-night: #140a18;
    --badge-ring: #ffffff;
    --badge-yellow: #ffd21f;
    --badge-orange: #f29a0c;
    --tagline-text: #ffffff;
    --tab-white: #ffffff;
    --tab-text: #222222;
    --name-box: #ffffff;
  }
  * { box-sizing: border-box; margin: 0; padding: 0; }
  html, body {
    width: 1200px;
    height: 899px;
    overflow: hidden;
    background: var(--page-bg);
  }
  .party-label {
    position: absolute;
    left: 330px;
    top: 90px;
    width: 540px;
    height: 720px;
    overflow: hidden;
    box-shadow: 0 10px 30px var(--label-shadow);
  }
  .party-scene {
    position: absolute;
    inset: 0;
    background:
      radial-gradient(ellipse at 50% 72%, rgba(255,255,255,0.3), transparent 45%),
      linear-gradient(180deg,
        var(--scene-dark) 0%,
        var(--scene-orange) 18%,
        var(--scene-amber) 30%,
        var(--scene-purple) 58%,
        var(--scene-pink) 72%,
        var(--scene-night) 100%);
  }
  .mascot-badge {
    position: absolute;
    left: 125px;
    top: 145px;
    width: 310px;
    height: 310px;
    border-radius: 50%;
    border: 12px solid var(--badge-ring);
    background: radial-gradient(circle at 40% 35%, var(--badge-yellow) 0%, var(--badge-yellow) 45%, var(--badge-orange) 100%);
  }
  .tagline {
    position: absolute;
    left: 0;
    right: 0;
    top: 468px;
    text-align: center;
    font-family: "Rammetto One", "Arial Black", sans-serif;
    font-size: 40px;
    line-height: 1.2;
    color: var(--tagline-text);
  }
  .tagline .line { display: block; }
  .name-field {
    position: absolute;
    left: 146px;
    top: 626px;
    width: 270px;
    height: 50px;
    background: var(--name-box);
  }
  .peel-tab {
    position: absolute;
    right: 0;
    top: 0;
    width: 100px;
    height: 100px;
  }
  .peel-tab text {
    font-family: "Roboto Mono", monospace;
    font-weight: 500;
    font-size: 13px;
    fill: var(--tab-text);
  }
</style>
</head>
<body>
  <main class="party-label">
    <div class="party-scene" role="img" aria-label="Party crowd dancing under colourful stage lights and fireworks"></div>
    <div class="mascot-badge" role="img" aria-label="Winking yellow smiley mascot"></div>
    <p class="tagline">
      <span class="line">For a good time,</span>
      <span class="line">peel me</span>
    </p>
    <div class="name-field"></div>
    <svg class="peel-tab" viewBox="0 0 100 100" aria-label="Peel here corner tab">
      <polygon points="0,0 100,0 100,100" fill="var(--tab-white)"/>
      <text x="58" y="40" text-anchor="middle" transform="rotate(45 58 40)">peel here</text>
    </svg>
  </main>
</body>
</html>
```